New website for a commercial real estate consulting company

What we’re looking for in a new web site:
• Desktop and mobile friendly
• Clear navigation
• Strong graphics
• Professional appearance
• The ability to update it ourselves
• Site is for information purposes only – no transactions required
• Traffic counts – number of visits per page?
• A firm quote on costs to develop and launch
• SSL
Attached is a copy of the revised text we propose to use, including our new logo. (The pagination can be different than as shown.)
Our current website address is www.brightlanecounselgroup.ca

```html
<!DOCTYPE html>
<html lang="en">
<head>
<meta charset="utf-8">
<title>Brightlane Counsel Group</title>
<link href="https://fonts.googleapis.com/css2?family=Roboto:wght@400;500;700&family=Kalam:wght@300&display=swap" rel="stylesheet">
<style>
  :root {
    --navy: #27358c;
    --indigo: #3c4697;
    --indigo-deep: #2a3584;
    --band-blue: #1d6ac6;
    --gold: #f3c544;
    --ink: #1f1f1f;
    --nav-text: #5a63a6;
    --footer-bg: #f4f5f9;
    --footer-text: #9a9cae;
    --white: #ffffff;
  }
  * { box-sizing: border-box; margin: 0; padding: 0; }
  html, body { width: 1200px; height: 1200px; overflow: hidden; background: var(--white); }
  body { font-family: "Roboto", Arial, sans-serif; color: var(--ink); position: relative; }
  .page { position: absolute; left: 214px; top: 0; width: 771px; height: 1200px; }

  .topbar { position: absolute; top: 0; left: 0; width: 100%; height: 26px; background: var(--navy); color: var(--white); font-size: 11px; }
  .topbar .phone { position: absolute; left: 13px; top: 6px; display: flex; align-items: center; gap: 4px; }
  .topbar .email { position: absolute; left: 249px; top: 5px; display: flex; align-items: center; gap: 5px; letter-spacing: .2px; }
  .topbar .social { position: absolute; right: 14px; top: 8px; display: flex; gap: 14px; }
  .topbar .social span { width: 10px; height: 10px; border-radius: 50%; background: var(--white); display: block; }

  .header { position: absolute; top: 26px; left: 0; width: 100%; height: 64px; background: var(--white); }
  .brand { position: absolute; left: 9px; top: 16px; display: flex; align-items: center; gap: 6px; }
  .brand .mark { width: 14px; height: 14px; background: var(--navy); }
  .brand .name { font-size: 10px; line-height: 12px; color: var(--navy); font-weight: 500; letter-spacing: .5px; text-transform: uppercase; }
  .nav { position: absolute; top: 24px; left: 0; width: 100%; font-size: 12.5px; color: var(--nav-text); }
  .nav a { position: absolute; color: inherit; text-decoration: none; transform: translateX(-50%); white-space: nowrap; }
  .nav a.active { color: var(--navy); font-weight: 500; }
  .nav a.active::after { content: ""; position: absolute; left: -3px; right: -3px; top: 21px; height: 2px; background: var(--navy); }
  .calendar { position: absolute; left: 726px; top: 18px; }

  .hero { position: absolute; top: 90px; left: 0; width: 100%; height: 448px; text-align: center; color: var(--white); }
  .hero .backdrop { position: absolute; inset: 0; background: linear-gradient(180deg, #5a64b3 0%, var(--indigo) 45%, var(--indigo-deep) 100%); }
  .hero .lead { position: absolute; top: 120px; width: 100%; font-family: "Kalam", cursive; font-weight: 300; font-size: 23px; letter-spacing: 1px; }
  .hero .claims { position: absolute; top: 165px; width: 100%; font-size: 24px; font-weight: 700; letter-spacing: 1.6px; }
  .hero .claims .dot { margin: 0 10px; }
  .hero .motto { position: absolute; top: 207px; width: 100%; font-size: 15px; color: var(--gold); letter-spacing: .3px; }
  .hero .scroll { position: absolute; left: 358px; top: 354px; }

  .intro-band { position: absolute; top: 538px; left: 0; width: 100%; height: 129px; background: var(--band-blue); color: var(--white); }
  .intro-band p { position: absolute; left: 56px; top: 27px; width: 510px; font-size: 10.3px; line-height: 15.4px; }
  .quote-btn { position: absolute; left: 578px; top: 44px; width: 139px; height: 41px; border-radius: 21px; background: var(--white); color: var(--navy); font-size: 12.5px; font-weight: 500; display: flex; align-items: center; justify-content: center; }

  .about { position: absolute; top: 726px; left: 57px; width: 280px; font-size: 10.3px; line-height: 15.4px; }
  .about p { margin-bottom: 15.4px; }
  .about ul { list-style: none; padding-left: 14px; }
  .about li::before { content: "•"; font-size: 7px; margin-right: 6px; position: relative; top: -1px; }
  .team-photo { position: absolute; left: 396px; top: 729px; width: 320px; height: 319px; background: linear-gradient(160deg, #e9e8e6 0%, #c9b3a2 45%, #6e6a6c 100%); box-shadow: 0 2px 6px rgba(0,0,0,.18); }

  .footer { position: absolute; top: 1110px; left: 0; width: 100%; height: 90px; background: var(--footer-bg); text-align: center; font-size: 9px; color: var(--footer-text); padding-top: 40px; }
</style>
</head>
<body>
<div class="page">
  <div class="topbar">
    <div class="phone">
      <svg width="9" height="9" viewBox="0 0 10 10"><path d="M2 0.5 L3.6 2.6 L2.8 3.6 Q4 6 6.4 7.2 L7.4 6.4 L9.5 8 L8.3 9.5 Q3.5 9 0.5 1.7 Z" fill="#fff"/></svg>
      905-555-0148
    </div>
    <div class="email">
      <svg width="11" height="8" viewBox="0 0 11 8"><rect width="11" height="8" rx="1" fill="#fff"/><path d="M0.5 0.8 L5.5 4.6 L10.5 0.8" stroke="#27358c" stroke-width="1.1" fill="none"/></svg>
      jordan.ellery@brightlanecounselgroup.ca
    </div>
    <div class="social"><span></span><span></span><span></span></div>
  </div>

  <div class="header">
    <div class="brand">
      <div class="mark"></div>
      <div class="name">Brightlane<br>Counsel Group</div>
    </div>
    <nav class="nav">
      <a class="active" style="left:352px">Home</a>
      <a style="left:452px">Who We Are</a>
      <a style="left:566px">What We Do</a>
      <a style="left:668px">Contact</a>
    </nav>
    <svg class="calendar" width="26" height="26" viewBox="0 0 26 26" fill="none" stroke="#27358c" stroke-width="1.2">
      <rect x="1" y="4" width="23" height="21" rx="1"/>
      <line x1="1" y1="9" x2="24" y2="9"/>
      <line x1="6" y1="1" x2="6" y2="6"/><line x1="10" y1="1" x2="10" y2="6"/><line x1="14" y1="1" x2="14" y2="6"/><line x1="18" y1="1" x2="18" y2="6"/>
      <g fill="#27358c" stroke="none">
        <rect x="5" y="12" width="3" height="3"/><rect x="9.5" y="12" width="3" height="3"/><rect x="14" y="12" width="3" height="3"/><rect x="18.5" y="12" width="3" height="3"/>
        <rect x="5" y="17" width="3" height="3"/><rect x="9.5" y="17" width="3" height="3"/><rect x="14" y="17" width="3" height="3"/><rect x="18.5" y="17" width="3" height="3"/>
      </g>
    </svg>
  </div>

  <section class="hero">
    <div class="backdrop" role="img" aria-label="Upward view of glass office towers tinted in blue"></div>
    <div class="lead">We are your choice for</div>
    <div class="claims">EXPERT<span class="dot">•</span>EXPERIENCED<span class="dot">•</span>COST EFFECTIVE</div>
    <div class="motto">Reputation is the currency of the 21st century</div>
    <svg class="scroll" width="56" height="56" viewBox="0 0 56 56" fill="none">
      <circle cx="28" cy="28" r="26" stroke="#f3c544" stroke-width="1.5"/>
      <path d="M21 22 L28 29 L35 22 M21 27 L28 34 L35 27 M21 32 L28 39 L35 32" stroke="#fff" stroke-width="1.3"/>
    </svg>
  </section>

  <section class="intro-band">
    <p><strong>Brightlane Counsel Group</strong> is an independent consulting firm offering practical, hands-on assistance to the commercial real estate and commercial mortgage lending industries.&nbsp; We specialize in financial analysis, underwriting and financial due diligence.<br>Working with us, you get top notch help when you need it – and only when you need it – one project at a time.</p>
    <div class="quote-btn">Get a Quote</div>
  </section>

  <section class="about">
    <p><strong>Brightlane Counsel Group</strong> has been providing expert, experienced and cost-effective service to the commercial real estate and commercial mortgage industries since 2001.&nbsp; We have worked on projects across Canada and the United States, and in every major property type.</p>
    <p>The foundation of our success has been our commitment to exceeding our clients’ expectations, both in quality and in timeliness.&nbsp; We strive to go above and beyond on every assignment.</p>
    <strong>Our clients include:</strong>
    <ul>
      <li>Chartered banks</li>
      <li>Mortgage bankers</li>
      <li>Public REITs &amp; REOCs</li>
      <li>Private equity firms</li>
      <li>Family-owned real estate investment companies</li>
      <li>Life insurance companies</li>
      <li>Pension funds</li>
      <li>Non-bank lenders</li>
      <li>Brokerage firms</li>
    </ul>
  </section>
  <div class="team-photo" role="img" aria-label="Team of colleagues seen from below joining hands in a star shape"></div>

  <footer class="footer">Copyright © Brightlane Counsel Group. All rights reserved.</footer>
</div>
</body>
</html>
```